Bath Salt - Sachet Packet (5 Scents) Packaging Design

We sell products to professional salons in the USA. This product is used as the first step when treating clients to a pedicure spa. This product is called SALT SOAK (or Bath Salts). The salt is added to the water to cleanse the skin, create a pleasant fragrance, and change the color of the water.

This product has 5 different variations, based on the scent of the salt soak. The available scents are:
LAVENDER, MANDARIN, CUCUMBER-MELON, JASMINE, MINT.

We would like to see package designs for all 5 scents. The theme should be consistent across the different variations of scents. The design should focus on bright, attractive, floral colors/themes. The design should fully express the color and imagery that are associated with each scent. (Lavender scent should include purple colors, lavender flower, etc.). See example images for reference of popular designs/brands.

Ideal designs will incorporate a luxurious and premium aesthetic that combines elegant imagery, colors, and premium finishes. See example images for reference of popular designs/brands.

Each packet is individually sealed. See dimension artwork file for reference of the sachet packet size and layout.

See the attached document guidelines for more information about product name, key text, and brand logo.

Target Market(s)

Beauty & Nail Salons

Industry/Entity Type

Beauty

Font styles to use
Sans Serif
Script

Requirements
Must have
• Bright imagery and colors that relate to the target fragrance
Nice to have
• Premium and luxurious finishes (shiny accent, etc.)

```html
<!DOCTYPE html>
<html lang="en">
<head>
<meta charset="utf-8">
<title>Lumo Sea Salt Soak – Mandarin Sachet</title>
<link href="https://fonts.googleapis.com/css2?family=Montserrat:wght@400;500;600;700;800&display=swap" rel="stylesheet">
<style>
  :root {
    --bg: #ffffff;
    --orange: #ec7420;
    --orange-deep: #c95a12;
    --fruit-light: #f7c45a;
    --fruit-mid: #f29a2e;
    --leaf: #9bb760;
    --gold-light: #f6e08a;
    --gold: #d9b04a;
    --gold-dark: #b88a2c;
    --ink: #1c1c1c;
    --text-light: #fff4e6;
  }
  * { margin: 0; padding: 0; box-sizing: border-box; }
  html, body { width: 1151px; height: 1200px; overflow: hidden; background: var(--bg); }
  body { position: relative; font-family: "Montserrat", sans-serif; }

  .sachet {
    position: absolute; left: 256px; top: 163px; width: 639px; height: 869px;
    border-radius: 10px; overflow: hidden;
  }
  .sachet__artwork {
    position: absolute; inset: 0;
    background:
      radial-gradient(circle at 15% 10%, var(--fruit-light) 0 8%, transparent 16%),
      radial-gradient(circle at 85% 12%, var(--fruit-mid) 0 9%, transparent 17%),
      radial-gradient(circle at 8% 55%, var(--fruit-light) 0 7%, transparent 15%),
      radial-gradient(circle at 92% 60%, var(--fruit-light) 0 7%, transparent 15%),
      radial-gradient(circle at 30% 95%, var(--fruit-mid) 0 8%, transparent 16%),
      radial-gradient(circle at 75% 93%, var(--leaf) 0 5%, transparent 12%),
      linear-gradient(160deg, #f4a53a 0%, #ee8526 50%, #f2b04a 100%);
  }

  .label {
    position: absolute; left: 107px; top: 142px; width: 420px; height: 645px;
    background: var(--orange);
    border: 1.5px solid var(--orange-deep);
    box-shadow: 0 0 0 4px var(--orange);
    color: var(--text-light);
  }
  .label__brand {
    position: absolute; top: 16px; left: 0; right: 0;
    display: flex; align-items: center; justify-content: center; gap: 8px;
    font-size: 38px; font-weight: 700; color: var(--ink); letter-spacing: 1px;
  }
  .label__brand-dot { width: 10px; height: 10px; background: var(--ink); border-radius: 50%; }
  .label__title {
    position: absolute; top: 68px; left: 0; right: 0; text-align: center;
    font-size: 40px; font-weight: 800; letter-spacing: 1.5px;
    background: linear-gradient(180deg, var(--gold-light) 0%, var(--gold) 55%, var(--gold-dark) 100%);
    -webkit-background-clip: text; background-clip: text; color: transparent;
  }
  .info-box {
    position: absolute; left: 20px; width: 385px;
    border: 1.5px solid var(--orange-deep);
    padding: 3px 8px;
    font-size: 12.6px; line-height: 20px; letter-spacing: 1.3px; text-transform: uppercase;
  }
  .info-box__heading { font-weight: 700; letter-spacing: 2px; }
  .line { display: block; white-space: nowrap; }
  .info-box--directions { top: 135px; height: 67px; }
  .info-box--ingredients { top: 213px; height: 108px; }
  .info-box--caution { top: 333px; height: 187px; }

  .distributor {
    position: absolute; left: 28px; top: 536px;
    font-size: 12.6px; line-height: 20.5px; letter-spacing: 1.3px;
  }
  .distributor__heading { font-weight: 700; letter-spacing: 2px; }
  .distributor__name { text-transform: uppercase; }
  .origin {
    position: absolute; left: 316px; top: 544px;
    font-size: 22px; line-height: 25px; font-weight: 400; color: #ffffff;
  }
</style>
</head>
<body>
  <div class="sachet">
    <div class="sachet__artwork" role="img" aria-label="Illustrated mandarin oranges, sliced orange halves and green leaves covering the packet"></div>

    <div class="label">
      <div class="label__brand"><span class="label__brand-dot"></span>Lumo</div>
      <h1 class="label__title">SEA SALT SOAK</h1>

      <section class="info-box info-box--directions">
        <p class="info-box__heading">Directions:</p>
        <p><span class="line">Add desired amount to warm water,soak</span><span class="line">feet, and then rinse.</span></p>
      </section>

      <section class="info-box info-box--ingredients">
        <p class="info-box__heading">Ingredients:</p>
        <p><span class="line">Lorem ipsum dolor sit amet, consectetur</span><span class="line">adipiscing elit, sed do eiusmod tempor</span><span class="line">incididunt ut labore et dolore magna</span><span class="line">aliqua.</span></p>
      </section>

      <section class="info-box info-box--caution">
        <p class="info-box__heading">Caution:</p>
        <p><span class="line">For external use only . Avoid use when</span><span class="line">skin is damaged or near any open cuts,</span><span class="line">wounds , or irritations. If signs of irri-</span><span class="line">tation occur, stop use immediately and</span><span class="line">consult a doctor . Keep away from</span><span class="line">direct sunlight. Store at room tempera-</span><span class="line">ture and use immediately after opening.</span><span class="line">Keep out of reach of children.</span></p>
      </section>

      <section class="distributor">
        <p class="distributor__heading">DISTRIBUTED BY:</p>
        <p class="distributor__name">Bright Harbor Supply, Inc.</p>
        <p class="distributor__name">Maplewood, IN 46000</p>
        <p>www.brightharborsupply.com</p>
      </section>

      <p class="origin">MADE<br>IN<br>KOREA</p>
    </div>
  </div>
</body>
</html>
```